International MultiIndustry Team Coaching Site

Hello Designers,
We need a redesign of the pages attached.
The design must be engaging and modern, with a focus on the user experience, particularly for the "observations" page. Because this is the main page of the website. It is to be used on a 10'' tablet or desktop, to record observations on the fly, so it must be intuitive and efficient.
The positioning of the metrics and observations and etc, are just a reference. you can switch it up if you feel there is a better way (PLEASE DO ;) ).

There are many categories (color coded with borders in the example hpt_6_observations.jpg) and observation metrics within each category. This is the Key page, because it is the One with the most interactions.

The user should know when it has selected a category (there should be some visual hint) and the different metric widgets should be accounted for.
There are 3: The time widget at the end, numerical widgets (recording more or less numbers), and boolean ones (selected or not).

For the numerical widgets, we show plus and minus characters, but you can change this, being creative, keeping in mind that it must work well on a mobile device and desktop, and must be intuitive and quick.

Set your creativity free with the login screen , home screen, categories secret, events screen, journaling and observations screen .

We would like the site/mobile version to have a very modern look. Something that would be found in very popular and user friendly apps.

***** The events, journaling, category and home screens are getting 2 much attention , please focus also on the observations screen *******
Imagine you are a psychologist tasked with observing the behaviour of teenagers during group work. And you have a tablet on which to record what you observe. Now imagine you need to observe during 3 classes: Biology, Math, Physics (these are events). For each class (event) you will have to record observations in 3 categories: Social Interaction, Leadership, Communication (these are categories).
Example of the metrics (these are observations) for Leadership:
" the teenager direct other colleagues" (boolean widget),
"the teenager speaks more than everyone else" (boolean widget)
"the teenager interrupts colleagues speaking" (number widget)
"the work took hh:mm" (time widget)

The observations screen can have any shape and form you think of. It doesn't need to be that single column with yes and nos, or that double column with the squared cards.
thank you.

Hope that was useful intel :)
Available for any questions you might have.
Good luck :)

Target Market(s)

Enterprise teams

Number of Pages Required

5+ page

Font styles to use
Sans Serif

Requirements
Must have
• Modern design

```html
<!DOCTYPE html>
<html lang="en">
<head>
<meta charset="utf-8">
<title>UI Screens – Team Coaching</title>
<link href="https://fonts.googleapis.com/css2?family=Poppins:wght@400;500;600;700;800&display=swap" rel="stylesheet">
<style>
:root{
  --board:#558bc5;
  --board-band:#4670a3;
  --screen:#f3f3f3;
  --card:#ffffff;
  --ink:#3a3a3a;
  --muted:#8a8a8a;
  --line:#e4e4e4;
  --field:#eeeeee;
  --primary:#4f86c6;
  --primary-soft:#e3edf8;
  --pink:#c9487a;
  --purple:#5b4a9b;
}
*{box-sizing:border-box;margin:0;padding:0}
html,body{width:922px;height:1200px;overflow:hidden}
body{font-family:"Poppins",sans-serif;color:var(--ink);background:var(--board);position:relative}
.board-bg{position:absolute;inset:0;width:922px;height:1200px}
.board-title{position:absolute;top:44px;left:0;width:922px;text-align:center;color:#fff;font-weight:800;font-size:64px;letter-spacing:-1px;line-height:1}

.screen{position:absolute;width:357px;height:225px;background:var(--screen);overflow:hidden;box-shadow:0 6px 16px rgba(20,40,80,.18)}
.screen > *{position:absolute}
.brand{left:26px;top:9px;font-size:8.5px;font-weight:600;color:#4a4a4a}
.toggle{left:267px;top:9px;width:16px;height:8px;border-radius:4px;background:#e2e2e2}
.toggle i{position:absolute;right:1px;top:1px;width:6px;height:6px;border-radius:50%;background:#fff}
.toggle::before{content:"";position:absolute;left:3px;top:3px;width:2px;height:2px;border-radius:50%;background:#aaa}
.avatar{left:291px;top:6px;width:13px;height:13px;border-radius:50%;background:var(--primary);color:#fff;font-size:5.5px;font-weight:600;display:flex;align-items:center;justify-content:center}
.greet{left:306px;top:9.5px;font-size:4.2px;font-weight:600}
.greet b{font-weight:400;color:#777;margin-left:2px}
.back{left:26px;top:31px;width:11px;height:11px;border-radius:50%;background:#e6e6e6;font-size:5px;color:#777;display:flex;align-items:center;justify-content:center}
.page-title{left:42px;top:33px;font-size:5.6px;font-weight:600}

/* home */
.tile{width:46px;height:54px;background:var(--card);border-radius:3px;box-shadow:0 1px 3px rgba(0,0,0,.05);display:flex;flex-direction:column;align-items:center;padding-top:9px}
.tile .ico{width:15px;height:15px;border-radius:50%;display:flex;align-items:center;justify-content:center}
.tile .lbl{font-size:3.7px;font-weight:600;text-align:center;margin-top:7px;line-height:1.3}
.tile .plus{width:14px;height:14px;border-radius:50%;background:#eeeeee;color:#666;font-size:7px;display:flex;align-items:center;justify-content:center;margin-top:5px}
.tile .tools{display:flex;gap:3px;margin-top:7px;align-self:flex-start;margin-left:8px}
.section-label{font-size:5px;font-weight:600}

/* login */
.login-card{left:103px;top:39px;width:152px;height:158px;background:var(--card);border-radius:3px;box-shadow:0 2px 8px rgba(0,0,0,.06)}
.login-card > *{position:absolute;left:15px}
.login-title{top:14px;left:0 !important;width:100%;text-align:center;font-size:11px;font-weight:700}
.login-sub{top:32px;left:0 !important;width:100%;text-align:center;font-size:4.2px;color:#666}
.field-label{font-size:3.8px;font-weight:600}
.field{width:122px;height:14px;background:var(--field);border-radius:1.5px;font-size:3.6px;color:#9a9a9a;padding-left:5px;display:flex;align-items:center}
.login-meta{width:122px;font-size:3.8px;color:#777;display:flex;justify-content:space-between;align-items:center}
.check{display:inline-block;width:5px;height:5px;background:#555;border-radius:1px;margin-right:2px;vertical-align:-1px}
.btn{background:var(--primary);color:#fff;font-weight:600;display:flex;align-items:center;justify-content:center;border-radius:1.5px}
.login-btn{width:122px;height:15px;font-size:4.2px}

/* events */
.event{top:50px;width:71px;height:107px;background:var(--card);border-radius:3px;overflow:hidden;box-shadow:0 1px 3px rgba(0,0,0,.05)}
.event .photo{height:53px}
.event h3{font-size:4.6px;font-weight:600;margin:7px 0 0 7px}
.event p{font-size:3.4px;color:#666;line-height:1.45;margin:2px 6px 0 7px}
.event .link{display:inline-block;margin:5px 0 0 7px;font-size:3.1px;font-weight:600;color:var(--primary);background:var(--primary-soft);padding:1.5px 4px;border-radius:1px}

/* metrics */
.metric{width:149px;background:var(--card);border-radius:3px;box-shadow:0 1px 3px rgba(0,0,0,.05);display:flex;align-items:center;justify-content:space-between;padding:0 9px}
.metric p{font-size:3.5px;color:#555;line-height:1.55;width:82px}
.stepper{width:38px;height:12px;background:#f1f3f6;border-radius:1.5px;display:flex;align-items:center;justify-content:space-around;font-size:4.6px;color:var(--primary);font-weight:600}
.select{width:38px;height:12px;border:.5px solid #e3e3e3;border-radius:1.5px;font-size:3.4px;color:var(--primary);display:flex;align-items:center;justify-content:space-between;padding:0 4px}

/* observation panel */
.panel{left:26px;top:50px;width:304px;background:var(--card);border-radius:3px;box-shadow:0 2px 6px rgba(0,0,0,.05)}
.panel > *{position:absolute}
.question{left:13px;top:12px;font-size:4.8px;font-weight:600}
.question em{font-style:normal;color:var(--primary)}
.textarea{left:13px;background:var(--field);border-radius:2px;font-size:3.6px;color:#8f8f8f;padding:5px 7px}
.tags{left:13px;display:flex;flex-wrap:wrap;gap:4px 3px;width:270px}
.tag{height:10px;padding:0 5px;border:.5px solid #dcdcdc;border-radius:1px;font-size:3.3px;font-weight:600;display:flex;align-items:center;background:#fff}
.tag.on{background:var(--primary-soft);color:var(--primary);border-color:var(--primary-soft)}
.panel-heading{left:13px;font-size:5px;font-weight:600}
.yn-row{left:13px;width:230px;display:flex;align-items:center;font-size:3.5px;color:#555}
.yn-row span:first-child{width:171px}
.yes,.no{width:19px;height:7px;font-size:3.3px;font-weight:700;display:flex;align-items:center;justify-content:center;margin-right:2px;border-radius:.5px}
.yes{background:var(--primary-soft);color:var(--primary)}
.no{background:var(--pink);color:#fff}

/* dashboard */
.chart-panel{background:var(--card);border-radius:3px;box-shadow:0 1px 4px rgba(0,0,0,.05)}
.seg{height:10px;font-size:3.4px;font-weight:600;display:flex;align-items:center;justify-content:center;border-radius:1px}
</style>
</head>
<body>

<svg class="board-bg" viewBox="0 0 1680 2187" preserveAspectRatio="none" aria-hidden="true">
  <rect width="1680" height="2187" fill="#558bc5"/>
  <polygon points="1680,10 1680,610 90,2187 0,2187 0,1690" fill="#4670a3"/>
</svg>

<h1 class="board-title">UI Screens</h1>

<!-- Home -->
<section class="screen" style="left:90px;top:168px">
  <span class="brand">Logo Here</span><span class="toggle"><i></i></span><span class="avatar">R</span><span class="greet">Hi Rowan<b>⌄</b></span>
  <div class="tile" style="left:26px;top:35px">
    <span class="ico" style="background:var(--primary)"><svg width="8" height="8" viewBox="0 0 10 10"><path d="M2 8 L2 6 L6.5 1.5 L8.5 3.5 L4 8 Z" fill="none" stroke="#fff" stroke-width=".9"/></svg></span>
    <span class="lbl" style="margin-top:8px">My Journaling</span>
  </div>
  <div class="tile" style="left:77px;top:35px">
    <span class="plus">+</span>
    <span class="lbl" style="margin-top:6px">Add New<br>Narrative</span>
  </div>
  <span class="section-label" style="left:26px;top:100px">All Teams</span>
  <div class="tile" style="left:26px;top:110px;height:56px">
    <span class="ico" style="background:var(--pink)"><svg width="8" height="8" viewBox="0 0 10 10"><circle cx="5" cy="3.5" r="2" fill="none" stroke="#fff" stroke-width=".9"/><path d="M1.5 9 Q5 5 8.5 9" fill="none" stroke="#fff" stroke-width=".9"/></svg></span>
    <span class="lbl" style="margin-top:6px">Grass Team</span>
    <span class="tools"><svg width="5" height="6" viewBox="0 0 5 6"><rect x=".3" y=".3" width="4.4" height="5.4" fill="none" stroke="#999" stroke-width=".5"/></svg><svg width="5" height="6" viewBox="0 0 5 6"><path d="M.5 6V3M2.5 6V1M4.5 6V2.5" stroke="#999" stroke-width=".6"/></svg><svg width="5" height="6" viewBox="0 0 5 6"><path d="M.5 1H4.5M1 1.3V5.7H4V1.3" fill="none" stroke="#999" stroke-width=".5"/></svg></span>
  </div>
  <div class="tile" style="left:77px;top:110px;height:56px">
    <span class="ico" style="background:var(--purple)"><svg width="8" height="8" viewBox="0 0 10 10"><rect x="1" y="2.5" width="8" height="5" fill="none" stroke="#fff" stroke-width=".9"/><path d="M5 2.5V7.5M1 5H9" stroke="#fff" stroke-width=".7"/></svg></span>
    <span class="lbl" style="margin-top:6px">Hard Court</span>
    <span class="tools"><svg width="5" height="6" viewBox="0 0 5 6"><path d="M.5 6V3M2.5 6V1M4.5 6V2.5" stroke="#999" stroke-width=".6"/></svg><svg width="5" height="6" viewBox="0 0 5 6"><path d="M.5 1H4.5M1 1.3V5.7H4V1.3" fill="none" stroke="#999" stroke-width=".5"/></svg></span>
  </div>
  <div class="tile" style="left:128px;top:110px;height:56px">
    <span class="plus">+</span>
    <span class="lbl" style="margin-top:6px">Add New<br>Team</span>
  </div>
</section>

<!-- Login -->
<section class="screen" style="left:475px;top:168px">
  <span class="brand">Logo Here</span><span class="toggle"><i></i></span><span class="avatar">R</span><span class="greet">Hi Rowan<b>⌄</b></span>
  <div class="login-card">
    <h2 class="login-title">Login Account</h2>
    <p class="login-sub">See your growth and get consulting support!</p>
    <span class="field-label" style="top:52px">Email address*</span>
    <span class="field" style="top:58px">Enter your email address</span>
    <span class="field-label" style="top:78px">Password*</span>
    <span class="field" style="top:84px;font-size:5px;color:#777">**********</span>
    <div class="login-meta" style="top:106px"><span><i class="check"></i>Remember me</span><span>Forgot your password?</span></div>
    <span class="btn login-btn" style="top:119px">COACH LOGIN</span>
  </div>
</section>

<!-- Events -->
<section class="screen" style="left:90px;top:416px">
  <span class="brand">Logo Here</span><span class="toggle"><i></i></span><span class="avatar">R</span><span class="greet">Hi Rowan<b>⌄</b></span>
  <span class="back">‹</span><span class="page-title">Grass Team</span>
  <article class="event" style="left:26px"><div class="photo" role="img" aria-label="Photo of a smiling professional at a desk in an office" style="background:linear-gradient(135deg,#6b5a4e,#2f2a28 60%,#8a7b70)"></div><h3>Event 1</h3><p>Event to reflect on how the team manages their work and how they can improve.</p><span class="link">Add Observation</span></article>
  <article class="event" style="left:104px"><div class="photo" role="img" aria-label="Photo of two colleagues reviewing documents together" style="background:linear-gradient(135deg,#cfc6bc,#7d6a5c 55%,#3b322d)"></div><h3>Event 2</h3><p>Event to reflect on how the team manages their work and how they can improve.</p><span class="link">Add Observation</span></article>
  <article class="event" style="left:182px"><div class="photo" role="img" aria-label="Photo of a team meeting around a laptop" style="background:linear-gradient(135deg,#b9b2aa,#5e5652 55%,#d9d3cc)"></div><h3>Event 3</h3><p>Event to reflect on how the team manages their work and how they can improve.</p><span class="link">Add Observation</span></article>
  <article class="event" style="left:260px"><div class="photo" role="img" aria-label="Photo of a team leader presenting to colleagues at a table" style="background:linear-gradient(135deg,#a38c78,#3f4d66 55%,#c8b8a8)"></div><h3>Event 4</h3><p>Event to reflect on how the team manages their work and how they can improve.</p><span class="link">Add Observation</span></article>
</section>

<!-- Metrics -->
<section class="screen" style="left:475px;top:416px">
  <span class="brand">Logo Here</span><span class="toggle"><i></i></span><span class="avatar">R</span><span class="greet">Hi Rowan<b>⌄</b></span>
  <span class="back">‹</span><span class="page-title">StepRise-Iteracao #1</span>
  <div class="metric" style="left:26px;top:52px;height:30px"><p>Lorem ipsum veriates per se the fox jumps over the lazy dog and catches...</p><span class="stepper"><span>−</span><span>0</span><span>+</span></span></div>
  <div class="metric" style="left:181px;top:52px;height:30px"><p>Lorem ipsum veriates per se the fox jumps over the lazy dog and catches...</p><span class="stepper"><span>−</span><span>0</span><span>+</span></span></div>
  <div class="metric" style="left:26px;top:87px;height:30px"><p>Lorem ipsum veriates per se the fox jumps over the lazy dog and catches...</p><span class="stepper"><span>−</span><span>0</span><span>+</span></span></div>
  <div class="metric" style="left:181px;top:87px;height:30px"><p>Lorem ipsum veriates per se the fox jumps over the lazy dog and catches...</p><span class="stepper"><span>−</span><span>0</span><span>+</span></span></div>
  <div class="metric" style="left:26px;top:123px;height:31px"><p style="width:132px">Aenean sollicitudin, lorem quis bibendum auctor, nisi elit consequat ipsum sagittis sem nibh id elit duis sed odio sit amet nibh vulputate cursus a sit amet mauris. Morbi accumsan ipsum velit.</p></div>
  <div class="metric" style="left:181px;top:123px;height:31px"><p>How long was the event ?</p><span class="select"><span>Select time</span><span>⌄</span></span></div>
</section>

<!-- Observations -->
<section class="screen" style="left:90px;top:664px">
  <span class="brand">Logo Here</span><span class="toggle"><i></i></span><span class="avatar">R</span><span class="greet">Hi Rowan<b>⌄</b></span>
  <span class="back">‹</span><span class="page-title">Grass Team</span>
  <div class="panel" style="height:141px">
    <p class="question"><em>Welcome! How are you?</em> What are you observing.today?</p>
    <div class="textarea" style="top:24px;width:277px;height:48px">Enter comments if any...</div>
    <div class="tags" style="top:81px">
      <span class="tag">Collaboration</span><span class="tag">Communication</span><span class="tag">Openness &amp; Ownership</span><span class="tag">Situational Awareness</span><span class="tag">Visualization</span><span class="tag" style="width:35px;justify-content:center">Limit WIP</span>
      <span class="tag">Manage Flow</span><span class="tag">Make Policies Explicit</span>
    </div>
    <span class="btn" style="left:127px;top:116px;width:49px;height:12px;font-size:3.3px">Save Team Information</span>
  </div>
</section>

<!-- Kanban -->
<section class="screen" style="left:90px;top:911px">
  <span class="brand">Logo Here</span><span class="toggle"><i></i></span><span class="avatar">R</span><span class="greet">Hi Rowan<b>⌄</b></span>
  <span class="back">‹</span><span class="page-title">Grass Team - Team Kanban</span>
  <div class="panel" style="height:162px">
    <span class="panel-heading" style="top:8px">Visualization</span>
    <div class="yn-row" style="top:20px"><span>Lorem ipsum veriates per se the fox jumps over the lazy dog and catches the rabbit</span><span class="yes">YES</span><span class="no">NO</span></div>
    <div class="yn-row" style="top:31px"><span>Lorem ipsum veriates per se the fox jumps over the lazy dog and catches the rabbit</span><span class="yes">YES</span><span class="no">NO</span></div>
    <div class="yn-row" style="top:42px"><span>Lorem ipsum veriates per se the fox jumps over the lazy dog and catches the rabbit</span><span class="yes">YES</span><span class="no">NO</span></div>
    <span class="panel-heading" style="top:59px">Other Observations</span>
    <div class="textarea" style="top:68px;width:277px;height:28px">Enter comments</div>
    <span class="btn" style="left:13px;top:100px;width:42px;height:12px;font-size:3.3px">Add Observations</span>
    <div class="tags" style="top:125px">
      <span class="tag on">Collaboration</span><span class="tag">Communication</span><span class="tag">Openness &amp; Ownership</span><span class="tag on">Situational Awareness</span><span class="tag" style="width:35px;justify-content:center">Limit WIP</span><span class="tag">Manage Flow</span>
      <span class="tag">Make Policies Explicit</span>
    </div>
  </div>
</section>

<!-- Dashboard -->
<section class="screen" style="left:475px;top:664px;height:302px">
  <span class="brand">Logo Here</span><span class="toggle"><i></i></span><span class="avatar">R</span><span class="greet">Hi Rowan<b>⌄</b></span>
  <span class="back">‹</span><span class="page-title">High Performance Teaming Challenge</span>

  <svg class="chart-panel" style="left:26px;top:49px" width="304" height="94" viewBox="0 0 553 172" font-family="Poppins, sans-serif">
    <rect width="553" height="172" rx="5" fill="#fff"/>
    <g font-size="5.5" fill="#999">
      <text x="28" y="13">• ALDER</text><text x="75" y="13">• BRIGHTWAY</text><text x="124" y="13">• CORVANE</text><text x="182" y="13">• ELTO</text><text x="222" y="13">• EXARA</text><text x="279" y="13">• GALEN</text><text x="322" y="13">• RIDGEFIELD-IO</text><text x="398" y="13">• MONTEO</text><text x="456" y="13">• SOLVANE</text>
    </g>
    <g font-size="6" fill="#aaa" text-anchor="end">
      <text x="20" y="39">100</text><text x="20" y="58">80</text><text x="20" y="77">60</text><text x="20" y="97">40</text><text x="20" y="116">20</text><text x="20" y="135">0</text><text x="20" y="155">-20</text>
    </g>
    <g fill="#4f86c6">
      <rect x="46" y="69" width="5" height="83"/><rect x="78" y="113" width="5" height="39"/><rect x="111" y="119" width="5" height="33"/><rect x="143" y="94" width="5" height="58"/><rect x="176" y="58" width="5" height="94"/><rect x="208" y="83" width="5" height="69"/><rect x="241" y="58" width="5" height="94"/><rect x="274" y="132" width="5" height="20"/><rect x="306" y="100" width="5" height="52"/><rect x="339" y="94" width="5" height="58"/><rect x="372" y="56" width="5" height="96"/><rect x="404" y="83" width="5" height="69"/><rect x="437" y="94" width="5" height="58"/><rect x="470" y="56" width="5" height="96"/><rect x="502" y="83" width="5" height="69"/>
    </g>
    <g fill="#c9487a">
      <rect x="59" y="129" width="5" height="23"/><rect x="91" y="119" width="5" height="33"/><rect x="124" y="101" width="5" height="51"/><rect x="156" y="106" width="5" height="46"/><rect x="189" y="129" width="5" height="23"/><rect x="221" y="106" width="5" height="46"/><rect x="254" y="132" width="5" height="20"/><rect x="287" y="132" width="5" height="20"/><rect x="319" y="101" width="5" height="51"/><rect x="352" y="106" width="5" height="46"/><rect x="385" y="129" width="5" height="23"/><rect x="417" y="106" width="5" height="46"/><rect x="450" y="106" width="5" height="46"/><rect x="483" y="129" width="5" height="23"/><rect x="515" y="106" width="5" height="46"/>
    </g>
    <g>
      <rect x="247" y="25" width="71" height="101" rx="2" fill="#fff" stroke="#eee"/>
      <text x="253" y="36" font-size="6" fill="#333">Iteracao #2</text>
      <g font-size="4.8" fill="#777">
        <text x="253" y="46">• Alder</text><text x="312" y="46" text-anchor="end">55</text>
        <text x="253" y="55">• Brightway</text><text x="312" y="55" text-anchor="end">21</text>
        <text x="253" y="64">• Corvane</text><text x="312" y="64" text-anchor="end">71</text>
        <text x="253" y="73">• Elto</text><text x="312" y="73" text-anchor="end">41</text>
        <text x="253" y="82">• Exara</text><text x="312" y="82" text-anchor="end">38</text>
        <text x="253" y="91">• Galen</text><text x="312" y="91" text-anchor="end">33</text>
        <text x="253" y="100">• Ridgefield-io</text><text x="312" y="100" text-anchor="end">20</text>
        <text x="253" y="109">• Monteo</text><text x="312" y="109" text-anchor="end">32</text>
        <text x="253" y="118">• Solvane</text><text x="312" y="118" text-anchor="end">40</text>
      </g>
    </g>
    <g font-size="6" fill="#999" text-anchor="middle">
      <text x="64" y="166">Apresentacao da Equipa</text><text x="175" y="166">Iteracao #1</text><text x="286" y="166">Iteracao #2</text><text x="396" y="166">Iteracao #3</text><text x="507" y="166">Iteracao #4</text>
    </g>
  </svg>

  <span class="seg" style="left:133px;top:160px;width:45px;background:var(--primary-soft);color:var(--primary)">Underperforming</span>
  <span class="seg" style="left:180px;top:160px;width:45px;background:#fff;border:.5px solid #ddd">Performing</span>

  <svg class="chart-panel" style="left:26px;top:181px" width="99" height="94" viewBox="0 0 180 172" font-family="Poppins, sans-serif">
    <rect width="180" height="172" rx="5" fill="#fff"/>
    <text x="90" y="20" font-size="8" font-weight="600" fill="#444" text-anchor="middle">Communication psychological security</text>
    <g stroke="#eee" stroke-width=".6"><path d="M18 40V100M34 40V100M50 40V100M66 40V100M82 40V100M98 40V100M114 40V100M130 40V100M146 40V100M162 40V100M18 55H162M18 70H162M18 85H162"/></g>
    <path d="M18 92 C30 86 40 96 52 90 S70 84 80 90 S98 92 106 72 S114 52 120 64 S134 88 146 84 S156 88 162 90 V100 H18Z" fill="#dce8f6"/>
    <path d="M18 92 C30 86 40 96 52 90 S70 84 80 90 S98 92 106 72 S114 52 120 64 S134 88 146 84 S156 88 162 90" fill="none" stroke="#4f86c6"/>
    <path d="M18 96 C34 90 50 98 66 94 S96 92 110 88 S140 96 162 94" fill="none" stroke="#aab4c8" stroke-width=".7"/>
    <rect x="88" y="38" width="38" height="17" rx="2" fill="#4f86c6"/><text x="92" y="50" font-size="7" fill="#fff">100k</text><text x="112" y="50" font-size="3.5" fill="#fff">24% ▴</text>
    <g font-size="5.5" fill="#888">
      <text transform="translate(22,140) rotate(-45)">Alder</text><text transform="translate(40,140) rotate(-45)">Brightway</text><text transform="translate(60,140) rotate(-45)">Corvane</text><text transform="translate(76,140) rotate(-45)">Elto</text><text transform="translate(94,140) rotate(-45)">Exara</text><text transform="translate(112,140) rotate(-45)">Galen</text><text transform="translate(130,140) rotate(-45)">Ridgefield-io</text><text transform="translate(148,140) rotate(-45)">Monteo</text><text transform="translate(166,140) rotate(-45)">Solvane</text>
    </g>
  </svg>

  <svg class="chart-panel" style="left:129px;top:181px" width="99" height="94" viewBox="0 0 180 172" font-family="Poppins, sans-serif">
    <rect width="180" height="172" rx="5" fill="#fff"/>
    <text x="90" y="20" font-size="8" font-weight="600" fill="#444" text-anchor="middle">Values and principles</text>
    <g stroke="#eee" stroke-width=".6"><path d="M18 40V100M34 40V100M50 40V100M66 40V100M82 40V100M98 40V100M114 40V100M130 40V100M146 40V100M162 40V100M18 55H162M18 70H162M18 85H162"/></g>
    <path d="M18 92 C30 86 40 96 52 90 S70 84 80 90 S98 92 106 72 S114 52 120 64 S134 88 146 84 S156 88 162 90 V100 H18Z" fill="#f6dde6"/>
    <path d="M18 92 C30 86 40 96 52 90 S70 84 80 90 S98 92 106 72 S114 52 120 64 S134 88 146 84 S156 88 162 90" fill="none" stroke="#c9487a"/>
    <path d="M18 96 C34 90 50 98 66 94 S96 92 110 88 S140 96 162 94" fill="none" stroke="#e3a6bd" stroke-width=".7"/>
    <rect x="88" y="38" width="38" height="17" rx="2" fill="#c9487a"/><text x="92" y="50" font-size="7" fill="#fff">100k</text><text x="112" y="50" font-size="3.5" fill="#fff">24% ▴</text>
    <g font-size="5.5" fill="#888">
      <text transform="translate(22,140) rotate(-45)">Alder</text><text transform="translate(40,140) rotate(-45)">Brightway</text><text transform="translate(60,140) rotate(-45)">Corvane</text><text transform="translate(76,140) rotate(-45)">Elto</text><text transform="translate(94,140) rotate(-45)">Exara</text><text transform="translate(112,140) rotate(-45)">Galen</text><text transform="translate(130,140) rotate(-45)">Ridgefield-io</text><text transform="translate(148,140) rotate(-45)">Monteo</text><text transform="translate(166,140) rotate(-45)">Solvane</text>
    </g>
  </svg>

  <svg class="chart-panel" style="left:232px;top:181px" width="99" height="94" viewBox="0 0 180 172" font-family="Poppins, sans-serif">
    <rect width="180" height="172" rx="5" fill="#fff"/>
    <text x="90" y="20" font-size="8" font-weight="600" fill="#444" text-anchor="middle">Roles and responsibilities</text>
    <g stroke="#eee" stroke-width=".6"><path d="M18 40V100M34 40V100M50 40V100M66 40V100M82 40V100M98 40V100M114 40V100M130 40V100M146 40V100M162 40V100M18 55H162M18 70H162M18 85H162"/></g>
    <path d="M18 92 C30 86 40 96 52 90 S70 84 80 90 S98 92 106 72 S114 52 120 64 S134 88 146 84 S156 88 162 90 V100 H18Z" fill="#e2def0"/>
    <path d="M18 92 C30 86 40 96 52 90 S70 84 80 90 S98 92 106 72 S114 52 120 64 S134 88 146 84 S156 88 162 90" fill="none" stroke="#5b4a9b"/>
    <path d="M18 96 C34 90 50 98 66 94 S96 92 110 88 S140 96 162 94" fill="none" stroke="#b3aad3" stroke-width=".7"/>
    <rect x="88" y="38" width="38" height="17" rx="2" fill="#5b4a9b"/><text x="92" y="50" font-size="7" fill="#fff">100k</text><text x="112" y="50" font-size="3.5" fill="#fff">24% ▴</text>
    <g font-size="5.5" fill="#888">
      <text transform="translate(22,140) rotate(-45)">Alder</text><text transform="translate(40,140) rotate(-45)">Brightway</text><text transform="translate(60,140) rotate(-45)">Corvane</text><text transform="translate(76,140) rotate(-45)">Elto</text><text transform="translate(94,140) rotate(-45)">Exara</text><text transform="translate(112,140) rotate(-45)">Galen</text><text transform="translate(130,140) rotate(-45)">Ridgefield-io</text><text transform="translate(148,140) rotate(-45)">Monteo</text><text transform="translate(166,140) rotate(-45)">Solvane</text>
    </g>
  </svg>
</section>

</body>
</html>
```